Atelier Vane Architecture business card

We need to update our business card. We do high end custom residential, hospitality, and wellness architecture. We focus on creating unique spaces and design around the five senses, believing that architecture's true impact is not on our surroundings, but within us. We would like to see designs are instill a sense of calm awe. They should be crisp, fresh, clean, authentic, & contemporary without being sterile, overworked, or harsh. White space is important. Alternative materials are an option if natural. We have created our own logo and would like designs to incorporate it. However, we are willing to see alternatives if the logo becomes a stumbling block and you have an alternate you suggest. Card must have the following information:
Atelier Vane Architecture, Inc.
742 Marbury Rd. NE Atlanta, GA 30319
Dominic K. Whitlow, AIA, NCARB, LEED AP BD+C
ateliervane.example

Target Market(s)

Higher net worth individuals with an appreciation for design, nature, sustainability,

Industry/Entity Type

Architect

Contact Information for Business Card

See above. The title of Owner or Architect is helpful but not necessary. Minimalism should trump additional information.

Font styles to use
Serif
Sans Serif

Requirements
Must have
• It should look professional. It must use logo
Should not have
• caligraphy, animals, anything that is cute,

```html
<!DOCTYPE html>
<html lang="en">
<head>
<meta charset="utf-8">
<title>Atelier Vane Architecture — Business Card</title>
<link rel="stylesheet" href="https://fonts.googleapis.com/css2?family=Noto+Serif:wght@400;700&display=swap">
<style>
  :root {
    --backdrop: #d9d9d9;
    --card: #ffffff;
    --green: #1b7a22;
    --green-dark: #11621a;
    --ink: #3a3a3a;
    --muted: #5a5a5a;
    --rule: #dddddd;
    --bar: #3d3d3d;
  }
  * { box-sizing: border-box; margin: 0; padding: 0; }
  html, body { width: 1200px; height: 1000px; overflow: hidden; }
  body {
    position: relative;
    background: var(--backdrop);
    font-family: "Noto Serif", Georgia, serif;
    color: var(--ink);
  }
  .card {
    position: absolute;
    left: 220px;
    width: 760px;
    background: var(--card);
    border-radius: 28px;
    overflow: hidden;
    box-shadow: 0 4px 14px rgba(0,0,0,0.25);
  }
  .card--front { top: 50px; height: 433px; }
  .card--back { top: 525px; height: 435px; }

  .brand-name {
    position: absolute;
    font-weight: 400;
    color: var(--ink);
    line-height: 1.2;
    white-space: nowrap;
  }
  .card--front .brand-name {
    left: 0; right: 0; top: 222px;
    text-align: center;
    font-size: 36px;
  }
  .card--back .brand-name {
    right: 44px; top: 586px;
    top: 584px;
    text-align: right;
    font-size: 22px;
  }
  .card--back .brand-name { top: 60px; }

  .front__web {
    position: absolute; left: 0; right: 0; top: 366px;
    text-align: center; font-size: 16px; color: var(--green);
  }

  .tab {
    position: absolute; left: 0; top: 211px;
    width: 12px; height: 40px;
    background: var(--green);
    border-radius: 0 5px 5px 0;
  }
  .person { position: absolute; left: 44px; top: 206px; }
  .person__name { font-size: 22px; font-weight: 700; color: var(--green); }
  .person__creds { font-size: 16px; color: var(--muted); margin-top: 2px; }

  .divider {
    position: absolute; left: 44px; right: 43px; top: 270px;
    height: 2px; background: var(--rule);
  }

  .contacts { position: absolute; left: 44px; top: 285px; list-style: none; }
  .contacts li {
    display: flex; align-items: center; gap: 8px;
    font-size: 16px; line-height: 22px; color: var(--muted);
  }
  .contacts svg { width: 14px; height: 14px; fill: var(--green); flex: none; }

  .office {
    position: absolute; right: 43px; top: 305px;
    text-align: right; font-size: 16px; line-height: 22px; color: var(--muted);
    font-style: normal;
  }
  .office__name { font-weight: 700; color: var(--green); }

  .footer-rule {
    position: absolute; left: 0; right: 0; top: 400px;
    height: 3px; background: var(--bar);
  }
  .footer-band {
    position: absolute; left: 0; right: 0; top: 407px; bottom: 0;
    background: linear-gradient(var(--green), var(--green-dark));
  }
</style>
</head>
<body>

<section class="card card--front" aria-label="Card front">
  <p class="brand-name">Atelier Vane Architecture</p>
  <p class="front__web">www.ateliervane.example</p>
</section>

<section class="card card--back" aria-label="Card back">
  <p class="brand-name">Atelier Vane Architecture</p>

  <span class="tab"></span>
  <div class="person">
    <p class="person__name">Dominic K. Whitlow</p>
    <p class="person__creds">AIA, NCARB, LEED AP BD+C</p>
  </div>

  <div class="divider"></div>

  <ul class="contacts">
    <li>
      <svg viewBox="0 0 16 16" aria-hidden="true"><path d="M3.5 1 6 4 4.6 5.6c.9 2.3 2.5 3.9 4.8 4.8L11 9l3 2.5-1.3 2.8C7 14 2 9 1.7 3.3z"/></svg>
      404.555.0184
    </li>
    <li>
      <svg viewBox="0 0 16 16" aria-hidden="true"><path d="M4 1h8v4H4zM1 6h14v6h-3v3H4v-3H1zm4 4v4h6v-4z"/></svg>
      404.555.0148
    </li>
    <li>
      <svg viewBox="0 0 16 16" aria-hidden="true"><path d="M1 3h14v1.2L8 9 1 4.2zM1 6l7 4.8L15 6v7H1z"/></svg>
      info@ateliervane.example
    </li>
    <li>
      <svg viewBox="0 0 16 16" aria-hidden="true"><path d="M8 1a7 7 0 1 0 0 14A7 7 0 0 0 8 1zm0 1.5c.8 0 1.7 1.6 2 4H6c.3-2.4 1.2-4 2-4zM2.6 7.3h2.6v1.4H2.6zm8.2 0h2.6v1.4h-2.6zM6 9.5h4c-.3 2.4-1.2 4-2 4s-1.7-1.6-2-4z"/></svg>
      www.ateliervane.example
    </li>
  </ul>

  <address class="office">
    <p class="office__name">Atelier Vane Architecture, Inc.</p>
    <p>742 Marbury Rd. NE</p>
    <p>Atlanta, GA 30319</p>
  </address>

  <div class="footer-rule"></div>
  <div class="footer-band"></div>
</section>

</body>
</html>
```